Boat Charter Power Point Template

Power Point Template for a Catalogue for a Boat Charter Company. In each slide there will be a main foto of the boat and then 3 mini photos plus all the aditional information of each boat. Here I attach 2 diferent presentations to get inspired

```html
<!DOCTYPE html>
<html lang="en">
<head>
<meta charset="utf-8">
<title>Boat Charter Catalogue – Slide 03</title>
<link rel="stylesheet" href="https://fonts.googleapis.com/css2?family=Jost:wght@400;600&family=Playfair+Display:wght@700;900&display=swap">
<style>
  :root {
    --frame-black: #000000;
    --panel-white: #fafafa;
    --ink: #111111;
    --title-light: #ffffff;
    --accent-blue: #4472c4;
    --sea-deep: #0b3a50;
    --sea-mid: #15607c;
    --sea-dark: #121417;
    --divider-grey: #5a6470;
  }
  * { box-sizing: border-box; margin: 0; padding: 0; }
  html, body {
    width: 1200px; height: 750px; overflow: hidden;
    background: var(--frame-black);
  }
  .slide {
    position: absolute; left: 0; top: 37.5px;
    width: 1200px; height: 675px;
    background: var(--panel-white);
    overflow: hidden;
    font-family: "Jost", "Futura", sans-serif;
    color: var(--ink);
  }
  .hero-photo {
    position: absolute; left: 425.6px; top: 0;
    width: 774.4px; height: 675px;
    background:
      radial-gradient(ellipse 60% 30% at 70% 75%, rgba(230,240,245,0.35), transparent 70%),
      linear-gradient(180deg, var(--sea-dark) 0%, var(--sea-deep) 38%, var(--sea-mid) 70%, var(--sea-deep) 100%);
  }
  .slide-title {
    position: absolute; left: 117px; top: 130px;
    font-family: "Playfair Display", Georgia, serif;
    font-weight: 700; font-size: 44px; line-height: 1; letter-spacing: -0.2px;
    white-space: nowrap;
    background: linear-gradient(90deg, var(--ink) 0 308.6px, var(--title-light) 308.6px 100%);
    -webkit-background-clip: text; background-clip: text;
    color: transparent;
  }
  .rule { position: absolute; height: 1px; }
  .rule--top { left: 0; top: 200.5px; width: 337.5px; background: var(--accent-blue); }
  .rule--specs { left: 115px; top: 420.5px; width: 401px;
    background: linear-gradient(90deg, var(--accent-blue) 0 310px, var(--divider-grey) 310px); }

  .bullets { position: absolute; list-style: none; }
  .bullets li { position: relative; padding-left: 20px; }
  .bullets li::before {
    content: "•"; position: absolute; left: 0; top: 0; font-size: 15px; line-height: 18px;
  }
  .seasons { left: 125px; top: 206px; }
  .seasons li { font-size: 15px; line-height: 18px; margin-bottom: 13px; }
  .season-price {
    display: block; color: var(--accent-blue);
    font-weight: 600; font-size: 11.5px; line-height: 14px;
  }
  .specs { left: 125px; top: 466px; width: 300px; }
  .specs li { font-size: 15px; line-height: 18px; margin-bottom: 12px; }
  .spec-value { position: absolute; left: 141px; top: 0; color: var(--accent-blue); }
  .spec-unit { font-size: 8.5px; font-style: italic; line-height: 0; vertical-align: 6px; margin-left: 3px; }
  .spec-note {
    display: block; margin-top: 1px; width: 216px;
    font-size: 10.3px; line-height: 10.5px;
  }
  .breadcrumb {
    position: absolute; left: 32px; top: 578px;
    transform: rotate(-90deg); transform-origin: 0 0;
    font-size: 10.5px; line-height: 12px; white-space: nowrap; color: var(--ink);
  }
  .breadcrumb-line {
    position: absolute; left: 28px; top: 586px;
    width: 1px; height: 52px; background: var(--ink);
  }
  .page-number {
    position: absolute; left: 11px; top: 640px;
    font-family: "Playfair Display", Georgia, serif;
    font-weight: 900; font-size: 19px; line-height: 24px;
  }
</style>
</head>
<body>
  <main class="slide">
    <div class="hero-photo" role="img" aria-label="Aerial photo of a white motor yacht cruising through deep blue sea, leaving a wide white wake"></div>

    <h1 class="slide-title">Slide Title Goes Here</h1>

    <div class="rule rule--top"></div>
    <ul class="bullets seasons">
      <li>High Season (Jun-Aug)<span class="season-price">€9000/day</span></li>
      <li>Mid Season (Apr-May/Sep-Oct)<span class="season-price">€9000/day</span></li>
      <li>Low Season (Nov-Mar)<span class="season-price">€9000/day</span></li>
    </ul>

    <div class="rule rule--specs"></div>
    <ul class="bullets specs">
      <li>Capacity:<span class="spec-value">12+3 crew</span></li>
      <li>Fuel Req:<span class="spec-value">€1450<span class="spec-unit">168ltrs/h</span></span></li>
      <li>Length/Beam:<span class="spec-value">27m/6m</span></li>
      <li>Included:
        <span class="spec-note">Lorem ipsum dolor sit amet, consectetuer adipiscing elit, sed diam nonummy nibh euismod tincidunt ut laoreet dolore magna aliquam erat.</span>
      </li>
    </ul>

    <div class="breadcrumb">Presentation Title / Section Title // Slide Title</div>
    <div class="breadcrumb-line"></div>
    <div class="page-number">03</div>
  </main>
</body>
</html>
```